Social Media Marketing company needs a logo (tweak) and business card design

We need to slightly tidy up our logo, mainly to make sure we have the right design file (AI file type) also if possible remove the text below, for the business card we would like to get a fun yet professional feeling since we focus on social media marketing as well as event management
Target Market(s)
All industry really, just trying to look fun and professional to every one.
Industry/Entity Type
Marketing
Contact Information for Business Card
The Business Card needed to be fun yet professional
Font styles to use
Sans Serif
Colors
85cae6
Requirements
Must have
- The Logo.
- On the Name area, please provide two spaces 1. for English and Chinese.
- Rest is English only.
- Do not include a post code space.
- Phone number.
- Also please add website address www.brellavo.com
Nice to have
- Some water marks would be nice.
- Also the slogan "bright moves every day"

```html
<!DOCTYPE html>
<html lang="en">
<head>
<meta charset="utf-8">
<title>Brellavo Business Card</title>
<link href="https://fonts.googleapis.com/css2?family=Noto+Sans+TC:wght@400;500&family=Open+Sans:wght@400;600&display=swap" rel="stylesheet">
<style>
  :root {
    --backdrop: #8a8a8a;
    --ink: #111111;
    --paper: #ffffff;
    --muted: #8c8c8c;
    --rule: #9a9a9a;
    --accent: #85cae6;
  }
  * { margin: 0; padding: 0; box-sizing: border-box; }
  html, body {
    width: 1200px; height: 950px; overflow: hidden;
    background: var(--backdrop);
    font-family: "Open Sans", Arial, sans-serif;
  }
  .card {
    position: absolute; left: 250px;
    width: 700px; height: 400px;
    box-shadow: 0 10px 24px rgba(0,0,0,0.35);
    overflow: hidden;
  }
  .card--front { top: 40px; background: var(--ink); }
  .card--back { top: 505px; background: var(--paper); }

  .front-brand {
    position: absolute; top: 150px; left: 0; width: 100%;
    text-align: center; color: var(--paper);
    font-size: 40px; font-weight: 400; letter-spacing: 1px;
  }
  .front-slogan {
    position: absolute; top: 240px; left: 0; width: 100%;
    text-align: center; color: var(--accent);
    font-size: 15px; letter-spacing: 5px; text-transform: lowercase;
  }

  .back-split { position: absolute; inset: 0; }
  .holder { position: absolute; top: 30px; left: 34px; color: var(--paper); }
  .holder-name { font-size: 22px; font-weight: 600; letter-spacing: 0.5px; line-height: 30px; }
  .holder-name-zh {
    font-family: "Noto Sans TC", "Open Sans", sans-serif;
    font-size: 17px; font-weight: 500; letter-spacing: 2px;
    color: var(--accent); line-height: 26px;
  }
  .holder-email { font-size: 15px; line-height: 24px; }

  .brand {
    position: absolute; top: 215px; left: 455px;
    color: var(--ink); font-size: 32px; font-weight: 400;
    display: flex; align-items: center; gap: 12px;
  }
  .brand-dot { width: 14px; height: 14px; border-radius: 50%; background: var(--accent); }

  .address {
    position: absolute; top: 292px; left: 230px; width: 175px;
    color: var(--muted); font-size: 15px; line-height: 27px; text-align: right;
  }
  .divider {
    position: absolute; top: 292px; left: 425px;
    width: 2px; height: 56px; background: var(--accent);
  }
  .contact {
    position: absolute; top: 292px; left: 445px;
    color: var(--ink); font-size: 15px; line-height: 27px;
  }
  .contact-line { display: flex; align-items: center; gap: 8px; }
  .contact-line svg { width: 16px; height: 16px; }
</style>
</head>
<body>

  <section class="card card--front">
    <div class="front-brand">Brellavo</div>
    <div class="front-slogan">bright moves every day</div>
  </section>

  <section class="card card--back">
    <svg class="back-split" viewBox="0 0 700 400" width="700" height="400">
      <polygon points="0,0 473.5,0 0,287.5" fill="#111111"/>
      <line x1="9" y1="282" x2="457" y2="10" stroke="#85cae6" stroke-width="3"/>
      <circle cx="9" cy="282" r="7" fill="#111111" stroke="#85cae6" stroke-width="2.5"/>
      <circle cx="457" cy="10" r="7" fill="#ffffff" stroke="#85cae6" stroke-width="2.5"/>
    </svg>

    <div class="holder">
      <div class="holder-name">MARA LINDQVIST</div>
      <div class="holder-name-zh" lang="zh-Hant">林瑪拉</div>
      <div class="holder-email">mara@brellavo.com</div>
    </div>

    <div class="brand"><span class="brand-dot"></span>Brellavo</div>

    <div class="address">
      <div>2741 Harbor Lane</div>
      <div>Glen Ridge, NY</div>
    </div>
    <div class="divider"></div>
    <div class="contact">
      <div class="contact-line">418 2296 7305
        <svg viewBox="0 0 16 16" aria-hidden="true">
          <path d="M2 5 Q8 1 14 5 L12 7 L10 6 L10 5 Q8 4 6 5 L6 6 L4 7 Z" fill="#111111"/>
          <rect x="4" y="8" width="8" height="6" rx="1" fill="#111111"/>
        </svg>
      </div>
      <div class="contact-line">www.brellavo.com
        <svg viewBox="0 0 16 16" aria-hidden="true">
          <circle cx="8" cy="8" r="7" fill="#111111"/>
          <circle cx="8" cy="8" r="2.5" fill="#85cae6"/>
        </svg>
      </div>
    </div>
  </section>

</body>
</html>
```